Hi everyone,
Bright Nest Homes is a business that renovates older houses into modern homes. I'm looking for a design that is clean and simple. It needs to show the client that renovating is a simple process. No more than 3 colours to be used thanks.

What I need:
1. Logo
2. Business card (one side)
3. Letter head (A4)

Looking forward to the designs!

Industry/Entity Type

Construction

Logo Text

Bright Nest Homes

Font styles to use
Sans Serif

Requirements
Must have
• Trading name: Bright Nest Homes
• Contact name: Declan Ferris
• Email: declanferris@brightnesthomes.com.au
• Tel: 0417 582 046
• Clean and simple
Nice to have
• If design might include a few tools. eg Hammer, paint roller etc.
Should not have
• Complicated design

```html
<!DOCTYPE html>
<html lang="en">
<head>
<meta charset="UTF-8">
<title>Bright Nest Homes — Letterhead</title>
<link href="https://fonts.googleapis.com/css2?family=Questrial&display=swap" rel="stylesheet">
<style>
  :root {
    --backdrop: #ffffff;
    --paper: #ffffff;
    --accent-orange: #f9af3d;
    --tint-grey: #e5e5e5;
    --band-grey: #666666;
    --ink: #333333;
    --ink-soft: #9a9a9a;
    --on-band: #ffffff;
  }
  * { margin: 0; padding: 0; box-sizing: border-box; }
  html, body {
    width: 1200px;
    height: 700px;
    overflow: hidden;
    background: var(--backdrop);
    font-family: "Questrial", sans-serif;
  }
  .canvas {
    position: relative;
    width: 1200px;
    height: 700px;
  }
  .letterhead {
    position: absolute;
    left: 374px;
    top: 30px;
    width: 452px;
    height: 640px;
    background: var(--paper);
    box-shadow: 0 4px 14px rgba(0, 0, 0, 0.18);
    overflow: hidden;
  }
  .block { position: absolute; }
  .block--grey { background: var(--tint-grey); }
  .block--orange { background: var(--accent-orange); }
  .block--band { background: var(--band-grey); }

  .brand {
    position: absolute;
    display: flex;
    align-items: flex-end;
    gap: 5px;
  }
  .brand__words { display: flex; flex-direction: column; }
  .brand__name {
    text-transform: uppercase;
    color: var(--ink);
    line-height: 1;
    white-space: nowrap;
  }
  .brand__tagline {
    color: var(--ink-soft);
    line-height: 1;
    white-space: nowrap;
  }
  .brand__square {
    background: var(--accent-orange);
    flex: none;
  }

  .brand--header { left: 36px; top: 36px; }
  .brand--header .brand__name { font-size: 11px; }
  .brand--header .brand__tagline { font-size: 6px; margin-top: 3px; }
  .brand--header .brand__square { width: 18px; height: 18px; margin-bottom: 10px; }

  .brand--footer { right: 18px; top: 567px; }
  .brand--footer .brand__name { font-size: 8px; color: var(--on-band); }
  .brand--footer .brand__tagline { font-size: 4.5px; color: #d8d8d8; margin-top: 2px; }
  .brand--footer .brand__square { width: 13px; height: 13px; margin-bottom: 8px; }
</style>
</head>
<body>
<div class="canvas">
  <div class="letterhead">
    <!-- header bars -->
    <div class="block block--grey" style="left:337px; top:20px; width:115px; height:16px;"></div>
    <div class="block block--grey" style="left:193px; top:31px; width:144px; height:4px;"></div>
    <div class="block block--grey" style="left:154px; top:65px; width:298px; height:21px;"></div>
    <div class="block block--orange" style="left:174px; top:36px; width:278px; height:36px;"></div>

    <div class="brand brand--header">
      <div class="brand__words">
        <span class="brand__name">Bright Nest Homes</span>
        <span class="brand__tagline">Clean and Simple</span>
      </div>
      <span class="brand__square"></span>
    </div>

    <!-- footer bars -->
    <div class="block block--grey" style="left:366px; top:518px; width:86px; height:22px;"></div>
    <div class="block block--grey" style="left:154px; top:538px; width:298px; height:16px;"></div>
    <div class="block block--band" style="left:0; top:554px; width:452px; height:53px;"></div>
    <div class="block block--grey" style="left:54px; top:609px; width:380px; height:19px;"></div>
    <div class="block block--grey" style="left:434px; top:609px; width:18px; height:31px;"></div>

    <div class="brand brand--footer">
      <div class="brand__words">
        <span class="brand__name">Bright Nest Homes</span>
        <span class="brand__tagline">Clean and Simple</span>
      </div>
      <span class="brand__square"></span>
    </div>
  </div>
</div>
</body>
</html>
```